Meridel Voyages Website Redesign

Read the Company mission statement and then help us redesign the website along the guidelines in the design brief and using the logo and fonts supplied.

The current meridel voyages website is very dated but has been very sucessful, we would like to invest in a brand refresh and site rebuild to bring the website up to 2018 standard.

We have using cut and paste from other travel websites made a pdf mock up of what sort of content we need on the pages and the lay out we like.

Target Market(s)

+45 Plus experienced meridel voyages, established, educated

Number of Pages Required

4 page

Font styles to use
Sans Serif

Requirements
Must have
• There is a full brief document and mock up, it must follow the brand guidelines
Nice to have
• There is a full brief document and mock up
Should not have
• Looks of a cheap cruise deal travel site

```html
<!DOCTYPE html>
<html lang="en">
<head>
<meta charset="utf-8">
<title>Meridel Voyages – Search Results</title>
<link href="https://fonts.googleapis.com/css2?family=Lato:wght@400;700&display=swap" rel="stylesheet">
<style>
:root{
  --blue:#3f8fd2;
  --blue-panel:rgba(62,140,205,.92);
  --navy:#0d1a2c;
  --navy-2:#13233a;
  --black:#000;
  --white:#fff;
  --grey:#e4e6e8;
  --grey-text:#555;
  --green:#6cbf6a;
  --red:#e3131b;
  --link:#3f8fd2;
}
*{box-sizing:border-box;margin:0;padding:0}
html,body{width:676px;height:1200px;overflow:hidden}
body{font-family:"Lato",sans-serif;background:var(--white);position:relative;color:#222}
.abs{position:absolute}

/* header */
.brand{left:140px;top:6px;color:var(--blue);font-size:13px;font-weight:700;letter-spacing:.5px;line-height:1}
.brand::after{content:"";display:block;width:62px;height:1.5px;background:var(--blue);margin-top:2px}
.subscribe{left:425px;top:5px;width:110px;height:10px;border-radius:5px;background:var(--green);color:#fff;font-size:4.6px;font-weight:700;text-align:center;line-height:10px}
.contact-row{left:425px;top:19px;display:flex;gap:2px;align-items:center}
.phone{height:10px;border:1px solid var(--blue);border-radius:5px;padding:0 4px 0 2px;font-size:5.5px;font-weight:700;display:flex;align-items:center;gap:2px;color:#222}
.soc{width:10px;height:10px;border:1px solid var(--blue);border-radius:50%}

.nav{left:0;top:34px;width:676px;height:16px;background:var(--blue);display:flex;justify-content:center;align-items:center;gap:9px}
.nav a{color:#fff;font-size:4.8px;text-decoration:none}

/* hero */
.hero{left:0;top:50px;width:676px;height:160px;background:linear-gradient(90deg,#1d3140 0%,#2b5873 30%,#3f7ea1 50%,#2a5670 75%,#3a3a38 100%)}
.panel{left:134px;top:50px;width:408px;height:100px;background:var(--blue-panel)}
.panel h1{position:absolute;left:0;right:0;top:9px;text-align:center;color:#fff;font-size:9.5px;font-weight:400}
.sel{position:absolute;height:17px;border:1px solid rgba(255,255,255,.85);color:#fff;font-size:5px;display:flex;align-items:center;padding-left:8px}
.sel::after{content:"";position:absolute;right:7px;top:6px;width:3px;height:3px;border-right:1px solid currentColor;border-bottom:1px solid currentColor;transform:rotate(45deg)}
.sel.light{background:#fff;color:#888}
.sel.light::after{display:none}
.btn-search{position:absolute;background:#000;color:#fff;font-size:5.5px;height:17px;display:flex;align-items:center;justify-content:center}
.adv{position:absolute;left:314px;top:110px;color:#fff;font-size:5px;display:flex;gap:8px;align-items:center}
.adv u{text-decoration:underline}

.strip{left:0;top:150px;width:676px;height:60px;background:rgba(10,20,30,.55)}
.strip .lbl{position:absolute;color:#fff;font-size:7px}

/* results bg */
.results-bg{left:0;top:210px;width:676px;height:712px;background:linear-gradient(180deg,#dfe6ea 0%,#f2f4f5 25%,#fdfdfd 60%,#fff 100%)}
.results-bg::before{content:"";position:absolute;left:0;top:0;width:120px;height:300px;background:linear-gradient(90deg,#8a8c86,rgba(255,255,255,0))}
.results-bg::after{content:"";position:absolute;right:0;top:0;width:130px;height:300px;background:linear-gradient(270deg,#a7c3d2,rgba(255,255,255,0))}

.toolbar{left:140px;top:219px;width:395px;height:18px}
.tb-ico{position:absolute;left:0;top:0;width:21px;height:18px;background:#000;display:flex;align-items:center;justify-content:center}
.tb-count{position:absolute;left:21px;top:0;width:147px;height:18px;background:var(--grey);font-size:5px;color:#555;padding-left:8px;line-height:18px}
.tb-sort{position:absolute;left:174px;top:0;font-size:5px;color:#555;line-height:18px}
.tb-sel{position:absolute;top:0;height:18px;background:var(--grey);font-size:5px;color:#666;padding-left:8px;line-height:18px}
.tb-sel::after{content:"";position:absolute;right:8px;top:6px;width:3px;height:3px;border-right:1px solid #666;border-bottom:1px solid #666;transform:rotate(45deg)}

.pager{left:221px;display:flex;align-items:center;gap:4px;font-size:5px;color:#555}
.pager .pb{height:9px;padding:0 8px;line-height:9px;color:#fff;background:var(--blue)}
.pager .pb.wide{width:30px;text-align:center;padding:0}
.pager .pb.dark{background:#000;width:30px;text-align:center;padding:0}
.pager .num{width:9px;height:9px;border:1px solid #999;text-align:center;line-height:7px;color:#333}
.pager .gap{width:4px}

/* cards */
.card{left:140px;width:395px;height:89px;background:#f3f3f3}
.card .media{position:absolute;left:0;top:0;width:104px;height:89px}
.card .arr{position:absolute;top:40px;width:8px;height:9px;background:#000;display:flex;align-items:center;justify-content:center}
.card .arr.l{left:1px}.card .arr.r{right:1px}
.card .title{position:absolute;left:104px;top:0;width:291px;height:21px;background:var(--blue);color:#fff;font-size:7.2px;padding-left:11px;line-height:21px}
.card .info{position:absolute;left:116px;top:25px;width:178px;font-size:4.3px;color:#333}
.card .info dl{display:grid;grid-template-columns:32px 1fr;row-gap:2.6px}
.card .info dt{font-weight:700}
.card .info dd{color:#666}
.card .info p{margin-top:3px;color:#666;line-height:6px}
.card .info a{color:var(--link);text-decoration:none;font-weight:700}
.card .tag{position:absolute;left:249px;top:25px;width:50px;text-align:right;font-size:4.3px;font-weight:700;color:#222}
.card .price{position:absolute;left:300px;top:21px;width:95px;height:68px;background:#000;color:#fff;padding:15px 0 0 12px;font-size:7px}
.card .price strong{display:block;color:var(--blue);font-size:9.5px;font-weight:400;margin:1px 0 6px}
.hot{left:131px;top:481px;width:32px;height:32px;border-radius:50%;background:var(--red);color:#fff;font-size:7.5px;font-weight:700;display:flex;align-items:center;justify-content:center}

/* footer */
.footer{left:0;top:922px;width:676px;height:278px;background:linear-gradient(180deg,var(--navy-2),#070f1b)}
.footer h3{position:absolute;color:var(--blue);font-size:7.5px;font-weight:400}
.footer .txt{position:absolute;color:#fff;font-size:4.6px;line-height:6.4px}
.flinks{position:absolute;left:98px;top:51px;display:grid;grid-template-columns:58px 58px;row-gap:5.3px;list-style:none}
.flinks li{color:#fff;font-size:4.6px;position:relative;padding-left:9px}
.flinks li::before{content:"";position:absolute;left:0;top:1.8px;width:2px;height:2px;border-radius:50%;background:#fff}
.field-lbl{position:absolute;color:#fff;font-size:4.6px}
.field{position:absolute;left:366px;width:104px;height:13px;background:#1b2c45;color:#8696ad;font-size:4.5px;line-height:13px;padding-left:4px}
.sub-btn{position:absolute;left:366px;top:154px;width:38px;height:10px;background:var(--blue);color:#fff;font-size:4.8px;text-align:center;line-height:10px}
.fsoc{position:absolute;top:48px;left:486px;display:flex;gap:6px}
.fsoc span{width:8px;height:8px;border-radius:50%;background:#fff}
.badge{position:absolute;background:#fff;border-radius:3px}
.foot-brand{left:97px;top:1144px;color:var(--blue);font-size:16px;font-weight:700;letter-spacing:.6px;line-height:1}
.foot-brand::after{content:"";display:block;width:69px;height:1.5px;background:var(--blue);margin-top:2px}
.copy{left:386px;top:1149px;color:#ccd;font-size:4.6px}
</style>
</head>
<body>

<!-- header -->
<div class="abs brand">MERIDEL VOYAGES</div>
<div class="abs subscribe">Subscribe to Our Newsletter</div>
<div class="abs contact-row">
  <div class="phone">
    <svg width="6" height="6" viewBox="0 0 10 10"><circle cx="5" cy="5" r="5" fill="#3f8fd2"/><path d="M3 2.5l1 1.5-.6.8a4 4 0 0 0 1.8 1.8l.8-.6 1.5 1-.6 1C4.6 8 2 5.4 2 3.1z" fill="#fff"/></svg>
    1800 614 552
  </div>
  <span class="soc"></span><span class="soc"></span><span class="soc"></span><span class="soc"></span><span class="soc"></span>
</div>

<nav class="abs nav">
  <a>Home</a><a>About Us</a><a>Our Cruises</a><a>Destinations</a><a>Cruise Search</a><a>Exclusive Offers</a><a>Brochures</a><a>Our Team</a><a>Contact Us</a>
</nav>

<!-- hero / search -->
<div class="abs hero" role="img" aria-label="Coastal cliffs and sea background photograph"></div>
<section class="abs panel">
  <h1>Search Results</h1>
  <div class="sel" style="left:7px;top:31px;width:95px">Any Destination</div>
  <div class="sel" style="left:107px;top:31px;width:94px">Any Sailing Date</div>
  <div class="sel" style="left:207px;top:31px;width:94px">Any Arrival Date</div>
  <div class="sel" style="left:307px;top:31px;width:94px">Any Arrival Port</div>
  <div class="sel" style="left:7px;top:53px;width:95px">Any Cruiseline</div>
  <div class="sel" style="left:107px;top:53px;width:94px">Any Ship</div>
  <div class="sel" style="left:207px;top:53px;width:94px">Any Duration</div>
  <div class="btn-search" style="left:307px;top:53px;width:94px">Search Cruises</div>
  <div class="sel light" style="left:7px;top:75px;width:194px">Optional Search Phrase</div>
  <div class="sel" style="left:207px;top:75px;width:94px">Any Cruise Types</div>
  <div class="adv" style="left:314px;top:79px"><u>Advanced</u>
    <svg width="10" height="8" viewBox="0 0 10 8"><path d="M1 4a3 3 0 0 1 5-2.2M9 4a3 3 0 0 1-5 2.2" stroke="#fff" fill="none" stroke-width="1"/><path d="M6 0.5l.6 1.8-1.9.3zM4 7.5l-.6-1.8 1.9-.3z" fill="#fff"/></svg>
    Reset Search</div>
</section>
<section class="abs strip">
  <span class="lbl" style="left:139px;top:15px">Route:</span>
  <div class="sel" style="left:182px;top:11px;width:153px">Preferred Start Port</div>
  <div class="sel" style="left:341px;top:11px;width:95px">Preferred End Port</div>
  <div class="sel" style="left:441px;top:11px;width:95px">Optional Stopover</div>
  <span class="lbl" style="left:139px;top:37px">Ship Size:</span>
  <div class="sel" style="left:182px;top:33px;width:153px">Any Ship Size</div>
  <span class="lbl" style="left:342px;top:37px">Theme:</span>
  <div class="sel" style="left:376px;top:33px;width:160px">Any Theme</div>
</section>

<!-- results -->
<div class="abs results-bg" role="img" aria-label="Soft sea and coastline background photograph"></div>
<div class="abs toolbar">
  <div class="tb-ico"><svg width="7" height="7" viewBox="0 0 10 10"><circle cx="4" cy="4" r="3" stroke="#fff" fill="none" stroke-width="1.4"/><path d="M6.3 6.3L9 9" stroke="#fff" stroke-width="1.4"/></svg></div>
  <div class="tb-count">30 Results Found</div>
  <div class="tb-sort">Sort By</div>
  <div class="tb-sel" style="left:200px;width:96px">Departure</div>
  <div class="tb-sel" style="left:301px;width:94px">Modify Search</div>
</div>
<div class="abs pager" style="top:258px">Showing 1 of 10 page<span class="gap"></span><span class="pb wide">First</span><span class="pb dark">Previous</span><span class="num">1</span><span class="num">2</span><span class="pb wide">Next</span><span class="pb wide">Last</span></div>

<article class="abs card" style="top:287px">
  <div class="media" role="img" aria-label="White cruise ship on blue sea photograph" style="background:linear-gradient(180deg,#5a8fb8,#2f6f9b 55%,#1f5577)"></div>
  <span class="arr l"><svg width="3" height="4"><path d="M3 0L0 2l3 2z" fill="#fff"/></svg></span><span class="arr r" style="left:95px"><svg width="3" height="4"><path d="M0 0l3 2-3 2z" fill="#fff"/></svg></span>
  <div class="title">Journey from spain to Portugal</div>
  <div class="tag">FLY, CRUISE,TOUR</div>
  <div class="info"><dl><dt>Cruiseline:</dt><dd>Heritage Sea Voyages</dd><dt>Ship:</dt><dd>Aurelia Star</dd><dt>Depart:</dt><dd>Australia</dd><dt>Arrive:</dt><dd>Australia</dd><dt>Dates:</dt><dd>09 May – 24 May 2019</dd><dt>Duration:</dt><dd>14 Nights</dd></dl>
  <p>On this 14 night cruise you will discover some of Portugal and Spain's lesser travelled southern reaches, then on to Morocco. <a>READ MORE</a></p></div>
  <div class="price">Per person from<strong>AU$9,450*</strong>Outside Cabin</div>
</article>

<article class="abs card" style="top:386.5px">
  <div class="media" role="img" aria-label="Route map of Spain and Portugal" style="background:linear-gradient(135deg,#d9e6c9,#c8dbe8 60%,#e9eef0)"></div>
  <span class="arr l"><svg width="3" height="4"><path d="M3 0L0 2l3 2z" fill="#fff"/></svg></span><span class="arr r" style="left:95px"><svg width="3" height="4"><path d="M0 0l3 2-3 2z" fill="#fff"/></svg></span>
  <div class="title">Journey from Spain to Portugal</div>
  <div class="tag">FLY, CRUISE,TOUR</div>
  <div class="info"><dl><dt>Cruiseline:</dt><dd>Heritage Sea Voyages</dd><dt>Ship:</dt><dd>Aurelia Star</dd><dt>Depart:</dt><dd>Australia</dd><dt>Arrive:</dt><dd>Australia</dd><dt>Dates:</dt><dd>09 May – 24 May 2019</dd><dt>Duration:</dt><dd>14 Nights</dd></dl>
  <p>On this 14 night cruise you will discover some of Portugal and Spain's lesser travelled southern reaches, then on to Morocco. <a>READ MORE</a></p></div>
  <div class="price">Per person from<strong>AU$9,450*</strong>Outside Cabin</div>
</article>

<article class="abs card" style="top:486px">
  <div class="media" role="img" aria-label="Hilltop palace at sunset photograph" style="background:linear-gradient(180deg,#5b4f8c,#c9728a 40%,#e0a055 65%,#3f6b2d)"></div>
  <span class="arr l"><svg width="3" height="4"><path d="M3 0L0 2l3 2z" fill="#fff"/></svg></span><span class="arr r" style="left:95px"><svg width="3" height="4"><path d="M0 0l3 2-3 2z" fill="#fff"/></svg></span>
  <div class="title">Journey from Spain to Portugal</div>
  <div class="tag">FLY, CRUISE,TOUR</div>
  <div class="info"><dl><dt>Cruiseline:</dt><dd>Heritage Sea Voyages</dd><dt>Ship:</dt><dd>Aurelia Star</dd><dt>Depart:</dt><dd>Australia</dd><dt>Arrive:</dt><dd>Australia</dd><dt>Dates:</dt><dd>09 May – 24 May 2019</dd><dt>Duration:</dt><dd>14 Nights</dd></dl>
  <p>On this 14 night cruise you will discover some of Portugal and Spain's lesser travelled southern reaches, then on to Morocco. <a>READ MORE</a></p></div>
  <div class="price">Per person from<strong>AU$9,450*</strong>Outside Cabin</div>
</article>
<div class="abs hot">HOT!</div>

<article class="abs card" style="top:585px">
  <div class="media" role="img" aria-label="Cruise ship lit at dusk photograph" style="background:linear-gradient(180deg,#3a6aa6,#7ea5d6 50%,#1c2f56)"></div>
  <span class="arr l"><svg width="3" height="4"><path d="M3 0L0 2l3 2z" fill="#fff"/></svg></span><span class="arr r" style="left:95px"><svg width="3" height="4"><path d="M0 0l3 2-3 2z" fill="#fff"/></svg></span>
  <div class="title">Fly Free! Grand Adriatic &amp; Aegean Experience</div>
  <div class="tag">FLY, CRUISE</div>
  <div class="info"><dl><dt>Cruiseline:</dt><dd>Heritage Sea Voyages</dd><dt>Ship:</dt><dd>Aurelia Star</dd><dt>Depart:</dt><dd>Australia</dd><dt>Arrive:</dt><dd>Australia</dd><dt>Dates:</dt><dd>09 May – 24 May 2019</dd><dt>Duration:</dt><dd>14 Nights</dd></dl>
  <p>You can Fly Free on this 18 night cruise when you book an Ocean View or above cabin - cruise from Venice to Athens. <a>READ MORE</a></p></div>
  <div class="price">Per person from<strong>AU$11,150*</strong>Outside Cabin</div>
</article>

<article class="abs card" style="top:685px">
  <div class="media" role="img" aria-label="Vintage map of the Adriatic region" style="background:linear-gradient(135deg,#e6d6ae,#b9cfc6 55%,#dcc99c)"></div>
  <span class="arr l"><svg width="3" height="4"><path d="M3 0L0 2l3 2z" fill="#fff"/></svg></span><span class="arr r" style="left:95px"><svg width="3" height="4"><path d="M0 0l3 2-3 2z" fill="#fff"/></svg></span>
  <div class="title">Fly Free! Grand Adriatic &amp; Aegean Experience</div>
  <div class="tag">FLY, CRUISE</div>
  <div class="info"><dl><dt>Cruiseline:</dt><dd>Heritage Sea Voyages</dd><dt>Ship:</dt><dd>Aurelia Star</dd><dt>Depart:</dt><dd>Australia</dd><dt>Arrive:</dt><dd>Australia</dd><dt>Dates:</dt><dd>09 May – 24 May 2019</dd><dt>Duration:</dt><dd>14 Nights</dd></dl>
  <p>You can Fly Free on this 18 night cruise when you book an Ocean View or above cabin - cruise from Venice to Athens. <a>READ MORE</a></p></div>
  <div class="price">Per person from<strong>AU$11,150*</strong>Outside Cabin</div>
</article>

<article class="abs card" style="top:784px">
  <div class="media" role="img" aria-label="Venetian bridge and canal photograph" style="background:linear-gradient(180deg,#7fb2e0,#d9c6a3 45%,#2f7a8a)"></div>
  <span class="arr l"><svg width="3" height="4"><path d="M3 0L0 2l3 2z" fill="#fff"/></svg></span><span class="arr r" style="left:95px"><svg width="3" height="4"><path d="M0 0l3 2-3 2z" fill="#fff"/></svg></span>
  <div class="title">Fly Free! Grand Adriatic &amp; Aegean Experience</div>
  <div class="tag">FLY, CRUISE</div>
  <div class="info"><dl><dt>Cruiseline:</dt><dd>Heritage Sea Voyages</dd><dt>Ship:</dt><dd>Aurelia Star</dd><dt>Depart:</dt><dd>Australia</dd><dt>Arrive:</dt><dd>Australia</dd><dt>Dates:</dt><dd>09 May – 24 May 2019</dd><dt>Duration:</dt><dd>14 Nights</dd></dl>
  <p>You can Fly Free on this 18 night cruise when you book an Ocean View or above cabin - cruise from Venice to Athens. <a>READ MORE</a></p></div>
  <div class="price">Per person from<strong>AU$11,150*</strong>Outside Cabin</div>
</article>

<div class="abs pager" style="top:893px">Showing 1 of 10 page<span class="gap"></span><span class="pb wide">First</span><span class="pb dark">Previous</span><span class="num">1</span><span class="num">2</span><span class="pb wide">Next</span><span class="pb wide">Last</span></div>

<!-- footer -->
<footer class="abs footer">
  <h3 style="left:98px;top:32px">Meridel Voyages</h3>
  <ul class="flinks">
    <li>Home</li><li>Meet Our Team</li><li>Our Cruises</li><li>Testimonials</li><li>Destinations</li><li>Contact Us</li><li>Cruise Search</li><li>About Us</li><li>Exclusive Offers</li><li>Community</li><li>FAQs</li><li>Careers</li><li>Privacy Policy</li><li>The World <small style="font-size:3.4px">(Residential)</small></li>
  </ul>

  <h3 style="left:237px;top:32px">Welcome</h3>
  <p class="txt" style="left:237px;top:51px;width:118px">Our Journeys are designed through personal experience and tailored with passion to ensure a premium, hassle-free travel experience. We select our favourite destinations and create itineraries to introduce you to vibrant cultures, exquisite cuisines, fascinating histories and the rich and unique scenery in our world. All prices are in Australian dollars unless specified.</p>
  <h3 style="left:237px;top:109px">Opening Hours:</h3>
  <p class="txt" style="left:237px;top:128px;width:118px">Our specialist team looks forward to assisting you between 8:30am - 5pm AEST Monday to Friday.</p>
  <p class="txt" style="left:237px;top:154px;width:118px">All times are Australian Eastern Standard Time</p>

  <h3 style="left:366px;top:32px">Newsletter Signup</h3>
  <p class="txt" style="left:366px;top:51px;width:110px">Sign up for our mailing list to get latest updates and offers.</p>
  <span class="field-lbl" style="left:366px;top:71px">EMAIL ADDRESS*</span>
  <div class="field" style="top:79px">Your email address</div>
  <span class="field-lbl" style="left:366px;top:98px">FIRST NAME*</span>
  <div class="field" style="top:106px">Your first name</div>
  <span class="field-lbl" style="left:366px;top:125px">LAST NAME*</span>
  <div class="field" style="top:133px">Your last name</div>
  <div class="sub-btn">Subscribe</div>
  <span class="field-lbl" style="left:366px;top:169px">* required</span>

  <h3 style="left:486px;top:32px">Contact</h3>
  <p class="txt" style="left:486px;top:51px;width:110px">Free Call: 1800 614 552</p>
  <p class="txt" style="left:486px;top:62px;width:110px">Phone: (07) 5521 4630</p>
  <p class="txt" style="left:486px;top:73px;width:110px">Fax: (07) 5521 4631</p>
  <p class="txt" style="left:486px;top:84px;width:120px">Email: sales@meridelvoyages.com.au</p>
  <div class="fsoc" style="top:98px"><span></span><span></span><span></span><span></span></div>
  <div class="badge" style="left:487px;top:129px;width:42px;height:29px"></div>
  <div class="badge" style="left:536px;top:129px;width:42px;height:29px"></div>
  <div class="badge" style="left:487px;top:166px;width:42px;height:29px"></div>
</footer>
<div class="abs foot-brand">MERIDEL VOYAGES</div>
<div class="abs copy">© Meridel Voyages 2007-2018. All Rights Reserved. Site map. Terms and Conditions.</div>

</body>
</html>
```